a simple functional website for an up and coming service industry business

hi ,i also require in store promotional items like business cards, flyers, Chatterbox page t-shirts for workers and want all these to have the same look and feel.i need my website to catch the eye .the idea i have in my head is something that will sell the service ,the website is a tool to get people to inquire , book or pay for an assembly service.we assemble flatpack furniture , outdoor furniture,playgrounds etc ,basically anything that comes with instructions,our biggest customer at the moment is Norvalt who we assemble nationally.i am looking for a website to be bright modern and simple to use the current website is www.brindleyfitouts.com which is dull with to many pages . i have already had a new logo designed by sketch harbour and it is lime green and sky blue in colour, a webiste i like is jobtrek q4 although it has lots of flash and my budget probably wouldn't allow that at the moment.

Target Market(s)

customer will be visiting the website to find out about the service we provide , then hopefully making contact,either booking a job or asking for a quote, i like the idea of the phone, email icons on the home screen

Industry/Entity Type

Industry

Requirements
Must have
• a contact icon: when you click on it the page with the name ,email address ,phone number, address pops up

a phone icon : when you click on it the 1300 number pops up
Nice to have
• my current website is with plume and it is www.brindleyfitouts.com

a website i really like the design of is jobtrek q4 and Norvalt

would like some pictures of modern furniture ,bbq's ,gym equipment ,playground equiptment
Should not have
• the career page or price page my current website .i don't want it on there anymore

```html
<!DOCTYPE html>
<html lang="en">
<head>
<meta charset="utf-8">
<title>Brindley Assembly &amp; Installation</title>
<link href="https://fonts.googleapis.com/css2?family=Quicksand:wght@500;700&family=Arimo:wght@400;700&display=swap" rel="stylesheet">
<style>
:root{
  --blue:#1a78c2;
  --lime:#8ab528;
  --text:#555;
  --dark:#2a2a2a;
  --rule:#dedede;
}
*{margin:0;padding:0;box-sizing:border-box}
html,body{width:1200px;height:1200px;overflow:hidden;background:#fff}
body{position:relative;font-family:"Arimo",Arial,sans-serif;color:var(--text)}
.topline{position:absolute;left:0;top:0;width:1200px;height:3px;background:var(--blue)}
.phone-tab{position:absolute;left:672px;top:0;width:410px;height:38px;background:var(--blue);border-radius:0 0 22px 22px;color:#fff;font:700 12.5px "Quicksand",sans-serif;letter-spacing:1px;display:flex;align-items:center;justify-content:center}
.brand{position:absolute;left:120px;top:98px;display:flex;align-items:center;gap:10px}
.brand-mark{width:20px;height:20px;background:var(--blue)}
.brand-name{font:700 18px "Quicksand",sans-serif;color:var(--lime);letter-spacing:.3px}
.nav{position:absolute;top:72px;right:119px;display:flex;gap:43px;font:700 15px "Quicksand",sans-serif;letter-spacing:1.4px;color:#333}
.nav .active{color:var(--lime)}
.hero{position:absolute;left:0;top:132px;width:1200px;height:440px;background:linear-gradient(120deg,#8c7a64 0%,#c49a66 35%,#b98a5a 60%,#8a97a3 80%,#5c6670 100%)}
.hero-band{position:absolute;left:0;top:0}
.hero-title{position:absolute;left:678px;top:176px;color:#fff;font:700 38px "Quicksand",sans-serif;letter-spacing:3px;line-height:42px}
.hero-title small{display:block;font-size:29px;letter-spacing:2.6px;line-height:34px}
.dots{position:absolute;left:555px;top:400px;display:flex;gap:8px}
.dots span{width:12px;height:12px;border-radius:50%;background:#ccc;opacity:.8}
.dots span:first-child{background:#999}
h2{font:700 17px "Quicksand",sans-serif;letter-spacing:1.5px;color:var(--blue);text-transform:uppercase}
h2 .lead{color:var(--lime)}
.welcome h2{position:absolute;left:120px;top:599px}
.welcome-photo{position:absolute;left:120px;top:647px;width:240px;height:190px;background:linear-gradient(160deg,#5c7a3c,#b48a5e 55%,#c9a27a)}
.welcome-text{position:absolute;left:373px;top:642px;width:377px;font-size:11.8px;line-height:18px;text-align:justify}
.welcome-text p{margin-bottom:18px}
.services h2{position:absolute;left:780px;top:599px}
.services-text{position:absolute;left:780px;top:642px;width:301px;font-size:11.6px;line-height:19px;text-align:justify}
.services-text p{margin-bottom:19px}
.services ul{list-style:none;margin-top:-1px}
.services li{position:relative;padding-left:17px;margin-bottom:19px;text-transform:uppercase;font-size:12px;letter-spacing:.2px}
.services li::before{content:"";position:absolute;left:0;top:6px;border-left:5px solid var(--lime);border-top:3.5px solid transparent;border-bottom:3.5px solid transparent}
.divider{position:absolute;left:120px;top:862px;width:960px;height:1px;background:var(--rule)}
.projects h2{position:absolute;left:120px;top:883px}
.project{position:absolute;top:937px;width:300px}
.project-photo{width:300px;height:150px}
.project-caption{display:flex;justify-content:space-between;align-items:center;margin-top:9px;font:700 15px "Quicksand",sans-serif;letter-spacing:1px;color:var(--lime)}
.plus{width:16px;height:16px}
.footer{position:absolute;left:0;top:1150px;width:1200px;height:50px;background:var(--dark)}
.legal{position:absolute;left:121px;top:6px;font:700 10.5px "Arimo",sans-serif;color:#aaa;line-height:20px}
.social{position:absolute;right:120px;top:15px;display:flex;gap:12px;font:700 11px "Arimo",sans-serif;color:#bbb}
</style>
</head>
<body>
<div class="topline"></div>
<div class="phone-tab">BRINDLEY ASSEMBLY &amp; INSTALLATION : 1300-555-018</div>

<div class="brand"><span class="brand-mark"></span><span class="brand-name">BRINDLEY ASSEMBLY</span></div>

<nav class="nav">
  <span class="active">HOME</span><span>ABOUT US</span><span>SERVICES</span><span>CONTACT</span>
</nav>

<section class="hero" role="img" aria-label="Wooden outdoor dining table and chairs set on a timber deck">
  <svg class="hero-band" width="1200" height="440" viewBox="0 0 1200 440"><polygon points="668,156 1200,156 1200,273 600,273" fill="#8ab528"/></svg>
  <div class="hero-title">DOMESTIC FIT OUT<small>OUTDOOR FURNITURE</small></div>
  <div class="dots"><span></span><span></span><span></span><span></span><span></span></div>
</section>

<section class="welcome">
  <h2><span class="lead">WELCOME TO</span> BRINDLEY ASSEMBLY &amp; INSTALLATION !</h2>
  <div class="welcome-photo" role="img" aria-label="Round timber garden table with folding chairs in a leafy courtyard"></div>
  <div class="welcome-text">
    <p>Brindley Assembly &amp; Installation are the ready to assemble fit out specialists. We assemble and install DIY flat pack indoor and outdoor furniture, across South East Queensland for the major retailers.</p>
    <p>We provide a reliable domestic or commercial service with professional and qualified installers.With the necessary builders licence, insurances and over 10 years experience in how to install, at Brindley Assembly &amp; Installation we make the job easy for you.</p>
    <p>CALL 1300 555 018 to discuss your requirements and one of our prompt installers will contact you in a jiffy.</p>
  </div>
</section>

<section class="services">
  <h2>OUR SERVICES</h2>
  <div class="services-text">
    <p>We install DIY flat packed indoor and outdoor living, across South East Queensland for the major retailers.We install DIY flat packed indoor and outdoor living, across South East Queensland for the major retailers.</p>
    <p>Our services include:</p>
    <ul><li>Commercial fit out</li><li>Domestic fit out</li></ul>
  </div>
</section>

<div class="divider"></div>

<section class="projects">
  <h2>RECENT PROJECTS</h2>
  <div class="project" style="left:120px">
    <div class="project-photo" role="img" aria-label="Wicker lounge set with white cushions beside a pool" style="background:linear-gradient(180deg,#9cb87a,#5a4638 55%,#d9cfc0)"></div>
    <div class="project-caption">Outdoor Furniture<svg class="plus" viewBox="0 0 16 16"><circle cx="8" cy="8" r="6.5" fill="none" stroke="#8ab528" stroke-width="1.3"/><path d="M8 4.5v7M4.5 8h7" stroke="#8ab528" stroke-width="1.3"/></svg></div>
  </div>
  <div class="project" style="left:449px">
    <div class="project-photo" role="img" aria-label="Timber framed outdoor sofa with grey and white cushions" style="background:linear-gradient(180deg,#8a7a6a,#a8703c 45%,#3e3e40 75%,#9a9a98)"></div>
    <div class="project-caption">Outdoor Furniture<svg class="plus" viewBox="0 0 16 16"><circle cx="8" cy="8" r="6.5" fill="none" stroke="#8ab528" stroke-width="1.3"/><path d="M8 4.5v7M4.5 8h7" stroke="#8ab528" stroke-width="1.3"/></svg></div>
  </div>
  <div class="project" style="left:779px">
    <div class="project-photo" role="img" aria-label="Wicker corner lounge beside a lake with a large boulder" style="background:linear-gradient(180deg,#e6ece8,#a9b7a8 45%,#6a5442 75%,#cfd0c6)"></div>
    <div class="project-caption">Outdoor Furniture<svg class="plus" viewBox="0 0 16 16"><circle cx="8" cy="8" r="6.5" fill="none" stroke="#8ab528" stroke-width="1.3"/><path d="M8 4.5v7M4.5 8h7" stroke="#8ab528" stroke-width="1.3"/></svg></div>
  </div>
</section>

<footer class="footer">
  <div class="legal">© 2013 BRINDLEY INSTALLATIONS PTY LTD<br>QBSA LICENCE NUMBER: 1234500</div>
  <div class="social"><span>Chatterbox</span><span>Chirpline</span><span>Orbit Plus</span><span>Pinboardly</span><span>ClipStream</span><span>Feed</span></div>
</footer>
</body>
</html>
```